Brindlewave.com website design

I need a basic website for www.brindlewave.com. Brindle Wave has been hosting websites since 2002 via partnership arrangement with Tessloft.com and Namequill.com. We do not do any design, only hosting for small companies and nonprofits. We are referring people to ArtHarbor and others to get their websites developed. Our website and pricing does not change often, but I need to be able to easily update the pricing and contact page.

Target Market(s)

Small company and non profit organizations

Industry/Entity Type

Utility

Coding

Coded - Design and coding required

Number of Pages Required

5+ page

Colors

Designer to choose colors to be used in the design.

Requirements
Must have
• Wordsmith format for easy content management. The logo attached. Contact us page with the following: Phone and fax are the same number: 877.514.2938. Email address is mybrindlewave@quorvix.com. Mailing address is 4816 E. Millhaven Rd #137, Larkfield, OR 97418.
Nice to have
• Some kind of badge or tag line on the home page that celebrates our 15th year of hosting without a single hosting without any downtime. We are are 15 year partners with Tessloft.com and Namequill.com. Website Design tab needs to reference ArtHarbor or others for all their website design needs. We provide no design or updating services. We will provide the developers FTP access to our dedicated Linux server. We do not provide email services other than redirects to their proprietary email or gmail, yahoo, etc. Needs a services and pricing tab. We provide domain registration services via our partnership with Namequill.com. We will want a way for them to submit a suggested domain name for us to verify if available. I might be able to get a link from Namequill.com to our account for you to include on that tab REGISTER DOMAIN. The tab buttons can be: WHO WE ARE, WHAT WE DO, WHEN YOU NEED US, WHERE TO REACH US. Maybe consider making the WHO, WHAT, WHEN and WHERE a dark blue color the rest of the text different color just so they stand out
Should not have
• A lot of animation that takes a long time to open. Clean and simple website.

```html
<!DOCTYPE html>
<html lang="en">
<head>
<meta charset="utf-8">
<title>Brindle Wave – Hosting Websites Since 2002</title>
<link rel="stylesheet" href="https://fonts.googleapis.com/css2?family=Archivo+Black&family=Roboto:wght@400;500;700;900&display=swap">
<style>
:root{
  --blue:#2f8fdc;
  --button:#3b8fe2;
  --navy:#16365e;
  --footer:#0c5bb0;
  --gold:#f2b431;
  --gold-dark:#c98a12;
  --grey:#eeeeee;
  --text:#1d1d1d;
  --muted:#555555;
  --white:#ffffff;
}
*{box-sizing:border-box;margin:0;padding:0}
html,body{width:1200px;height:2440px;overflow:hidden}
body{font-family:"Roboto",Arial,sans-serif;color:var(--text);background:var(--white);position:relative}

.topbar{height:40px;background:var(--blue);color:var(--white);font-size:14px;display:flex;align-items:center;justify-content:space-between;padding:0 28px}
.topbar .contact{display:flex;gap:26px;align-items:center}
.topbar .item{display:flex;align-items:center;gap:8px}

.header{height:160px;display:flex;align-items:center;padding:0 30px}
.brand{display:flex;align-items:center;gap:12px;font-weight:700;font-size:26px;color:var(--navy);letter-spacing:.5px}
.brand .mark{width:34px;height:34px;border-radius:50%;background:var(--blue)}
.nav{display:flex;gap:48px;margin-left:110px;font-size:17px;font-weight:500;color:var(--navy)}

.hero{height:500px;position:relative;background:radial-gradient(ellipse at 65% 45%,#f4f4f4 0%,#b9bcc0 40%,#4c5156 80%,#2c3034 100%)}
.badge{position:absolute;left:70px;top:530px;width:210px;height:210px;border-radius:50%;background:var(--gold);border:8px solid var(--gold-dark);display:flex;flex-direction:column;align-items:center;justify-content:center;color:var(--white);z-index:2}
.badge .num{font-size:78px;font-weight:900;line-height:1}
.badge .lbl{font-size:16px;font-weight:700;letter-spacing:2px}

.intro{height:220px;display:flex;align-items:center;padding:0 30px}
.intro h1{font-size:34px;font-weight:700;line-height:1.15;width:290px;margin-top:24px}
.intro p{font-size:16px;line-height:1.5;width:470px;margin-left:30px;color:var(--muted)}
.btn{display:inline-block;background:var(--button);color:var(--white);font-size:15px;font-weight:500;padding:18px 40px;border-radius:2px}
.intro .btn{margin-left:auto;margin-right:8px;width:220px;text-align:center}

.offer{height:780px;background:var(--grey);text-align:center;padding-top:120px}
.section-title{font-family:"Archivo Black",Arial,sans-serif;font-size:36px;letter-spacing:1px;color:var(--text)}
.offer .lead{width:860px;margin:44px auto 0;font-size:17px;line-height:1.55;color:#333}
.cards{display:flex;justify-content:center;gap:110px;margin-top:70px}
.card{width:290px}
.card .icon{width:56px;height:56px;margin:0 auto}
.card h3{font-size:23px;font-weight:700;margin-top:12px}
.card p{font-size:15px;line-height:1.4;color:#444;margin:16px auto 0;width:270px}
.card .btn{margin-top:26px;width:210px;padding:16px 0}

.partners{height:500px;text-align:center;padding-top:110px}
.partners .sub{font-size:18px;margin-top:8px;color:#333}
.logos{display:flex;justify-content:space-around;align-items:center;margin-top:100px;padding:0 60px}
.partner-name{font-size:30px;font-weight:700;color:var(--text)}

.footer{height:240px;background:var(--footer);color:var(--white);position:relative;padding:40px 28px}
.footer .fnav{display:flex;gap:34px;font-size:15px;font-weight:500}
.footer .fcontact{display:flex;gap:30px;font-size:14px;margin-top:20px}
.footer .fcontact .item{display:flex;align-items:center;gap:8px}
.footer .addr{font-size:14px;margin-top:18px}
.footer .fbrand{position:absolute;right:30px;top:70px;display:flex;flex-direction:column;align-items:center;gap:10px;font-weight:700;font-size:20px}
.footer .fbrand .mark{width:70px;height:70px;background:var(--white)}
</style>
</head>
<body>

<div class="topbar">
  <div class="contact">
    <span class="item">
      <svg width="16" height="12" viewBox="0 0 16 12"><rect x="0.5" y="0.5" width="15" height="11" fill="none" stroke="#fff"/><path d="M1 1l7 6 7-6" fill="none" stroke="#fff"/></svg>
      mybrindlewave@quorvix.com
    </span>
    <span class="item">
      <svg width="14" height="14" viewBox="0 0 14 14"><path d="M3 1l2 3-1.5 1.5a8 8 0 0 0 5 5L10 9l3 2-1 2.5C6 13 1 8 .5 2z" fill="#fff"/></svg>
      877.514.2938
    </span>
  </div>
  <span>4816 E. Millhaven Rd #137, Larkfield, OR 97418</span>
</div>

<header class="header">
  <div class="brand"><span class="mark"></span>Brindle Wave</div>
  <nav class="nav">
    <span>HOME</span><span>ABOUT</span><span>SERVICES</span><span>PRICING</span><span>CONTACT</span>
  </nav>
</header>

<section class="hero" role="img" aria-label="Photo of a hand touching a glowing digital interface with a world map and charts"></section>

<div class="badge" aria-label="15 years anniversary badge"><span class="num">15</span><span class="lbl">YEARS</span></div>

<section class="intro">
  <h1>Hosting Websites Since 2002</h1>
  <p>Et harum quidem rerum facilis est et expedita distinctio. Nam libero tempore, cum soluta nobis est eligendi optio cumque nihil impedit quo minus id quod maxime.</p>
  <span class="btn">READ MORE</span>
</section>

<section class="offer">
  <h2 class="section-title">WHAT WE OFFER</h2>
  <p class="lead">Ut enim ad minima veniam, quis nostrum exercitationem ullam corporis suscipit laboriosam, nisi ut aliquid ex ea commodi consequatur? Quis autem vel eum iure reprehenderit qui in ea voluptate velit esse quam nihil molestiae consequatur, vel illum qui dolorem eum fugiat quo voluptas nulla pariatur</p>
  <div class="cards">
    <div class="card">
      <svg class="icon" viewBox="0 0 56 56"><circle cx="28" cy="28" r="27" fill="#16365e"/><rect x="18" y="16" width="20" height="7" rx="1" fill="#fff"/><rect x="18" y="25" width="20" height="7" rx="1" fill="#fff"/><rect x="18" y="34" width="20" height="7" rx="1" fill="#fff"/></svg>
      <h3>Web Site Hosting</h3>
      <p>Sed ut perspiciatis unde omnis iste natus error sit voluptatem accusantium doloremque laudantium.</p>
      <span class="btn">READ MORE</span>
    </div>
    <div class="card">
      <svg class="icon" viewBox="0 0 56 56"><circle cx="28" cy="28" r="27" fill="#16365e"/><circle cx="28" cy="28" r="13" fill="none" stroke="#fff" stroke-width="2.5"/><path d="M15 28h26M28 15c-6 7-6 19 0 26M28 15c6 7 6 19 0 26" fill="none" stroke="#fff" stroke-width="2"/></svg>
      <h3>Domain Registration</h3>
      <p>Sed ut perspiciatis unde omnis iste natus error sit voluptatem accusantium doloremque laudantium.</p>
      <span class="btn">READ MORE</span>
    </div>
    <div class="card">
      <svg class="icon" viewBox="0 0 56 56"><circle cx="28" cy="28" r="27" fill="#16365e"/><path d="M20 25h16M32 20l5 5-5 5M36 33H20M24 28l-5 5 5 5" fill="none" stroke="#fff" stroke-width="2.5"/></svg>
      <h3>FTP Access</h3>
      <p>Sed ut perspiciatis unde omnis iste natus error sit voluptatem accusantium doloremque laudantium.</p>
      <span class="btn">READ MORE</span>
    </div>
  </div>
</section>

<section class="partners">
  <h2 class="section-title">OUR PARTNERS</h2>
  <p class="sub">We are 15 years in partners with</p>
  <div class="logos">
    <span class="partner-name">Tessloft</span>
    <span class="partner-name">Namequill.com</span>
    <span class="partner-name">ArtHarbor</span>
  </div>
</section>

<footer class="footer">
  <nav class="fnav"><span>HOME</span><span>ABOUT</span><span>SERVICES</span><span>PRICING</span><span>CONTACT</span></nav>
  <div class="fcontact">
    <span class="item">
      <svg width="16" height="12" viewBox="0 0 16 12"><rect x="0.5" y="0.5" width="15" height="11" fill="none" stroke="#fff"/><path d="M1 1l7 6 7-6" fill="none" stroke="#fff"/></svg>
      mybrindlewave@quorvix.com
    </span>
    <span class="item">
      <svg width="14" height="14" viewBox="0 0 14 14"><path d="M3 1l2 3-1.5 1.5a8 8 0 0 0 5 5L10 9l3 2-1 2.5C6 13 1 8 .5 2z" fill="#fff"/></svg>
      877.514.2938
    </span>
  </div>
  <p class="addr">4816 E. Millhaven Rd #137, Larkfield, OR 97418</p>
  <div class="fbrand"><span class="mark"></span>Brindle Wave</div>
</footer>

</body>
</html>
```